A property investment company, looking to provide lovely sustainable homes for familys and individua

For a small investment business i am starting which will buy and refurbish unloved houses and apartments to rent out or resell. the company name is my family surname (HARGREAVE). <br/>i would like the design to be simple with maybe some emphasis on an ethical and sustainable/environmentally friendly approach with a branding of maybe trees blended with some houses and or apartments.<br/>The colours i like for this design would be mainly green on either a white or black background.
Target Market(s)
This business card is to be used for professional people such as estate agents
mortgage brokers, solicitors and trades people.
Industry/Entity Type
Real Estate
Contact Information for Business Card
owner/director-Martin hargreave
e-mail-martin@hvholdings.co.uk
website-hargreavehomeholdings.co.uk
mobile-07700945318
landline-02079460581
Look and feel

```html
<!DOCTYPE html>
<html lang="en">
<head>
<meta charset="utf-8">
<title>Hargreave Property Investments – Business Card</title>
<link href="https://fonts.googleapis.com/css2?family=Saira:wght@300;400;600&display=swap" rel="stylesheet">
<style>
  :root{
    --backdrop:#1c201e;
    --green-deep:#2e9a5c;
    --green-mid:#58ad72;
    --green-soft:#7fc08f;
    --green-pale:#a9d4b3;
    --green-mist:#d3e9d8;
    --paper:#f1f2f1;
    --ink-green:#2b9455;
    --ink-light:#8fcb64;
    --white:#ffffff;
  }
  *{box-sizing:border-box;margin:0;padding:0}
  html,body{width:1200px;height:1190px;overflow:hidden}
  body{
    background:var(--backdrop);
    font-family:"Saira",sans-serif;
    display:flex;flex-direction:column;align-items:center;justify-content:center;gap:70px;
  }
  .card{
    position:relative;width:700px;height:400px;overflow:hidden;
    box-shadow:0 20px 40px rgba(0,0,0,.45);
  }
  .block{position:absolute}

  /* front */
  .card-front{background:var(--green-deep)}
  .front-top-left{left:0;top:0;width:260px;height:145px;background:var(--green-pale)}
  .front-top-mid{left:260px;top:0;width:210px;height:145px;background:var(--green-mist)}
  .front-bottom-left{left:0;top:145px;width:260px;height:255px;background:var(--green-mid)}
  .front-mid-square{left:260px;top:145px;width:210px;height:125px;background:var(--green-mist)}
  .hatch{position:absolute;right:0;top:0;width:38px;height:400px}
  .front-brand{position:absolute;left:300px;top:274px;color:var(--white)}
  .brand-name{font-weight:600;font-size:50px;letter-spacing:4px;line-height:1}
  .brand-tagline{font-weight:300;font-size:15px;letter-spacing:3.2px;margin-top:8px}

  /* back */
  .card-back{background:var(--paper)}
  .back-band-top{right:0;top:0;width:200px;height:200px;background:var(--green-pale)}
  .back-band-bottom{right:0;top:200px;width:200px;height:200px;background:var(--green-soft)}
  .back-brand{position:absolute;left:56px;top:52px;color:var(--ink-green)}
  .back-brand .brand-name{font-size:44px}
  .back-brand .brand-tagline{font-size:13px;color:var(--ink-light);font-weight:400;margin-top:6px}
  .contact{position:absolute;left:56px;top:170px;color:var(--ink-green);font-weight:400;font-size:19px;line-height:1.5;letter-spacing:.5px}
  .contact-name{font-size:24px;line-height:1.3}
  .contact-role{font-size:11px;letter-spacing:3px;color:var(--ink-light);margin-bottom:12px}
</style>
</head>
<body>
  <section class="card card-front" aria-label="Business card front">
    <div class="block front-top-left"></div>
    <div class="block front-top-mid"></div>
    <div class="block front-bottom-left"></div>
    <div class="block front-mid-square"></div>
    <svg class="hatch" viewBox="0 0 38 400" aria-hidden="true">
      <defs>
        <pattern id="stripe" width="6" height="6" patternUnits="userSpaceOnUse" patternTransform="rotate(45)">
          <line x1="0" y1="0" x2="0" y2="6" stroke="#8fcf9f" stroke-width="1.4"/>
        </pattern>
      </defs>
      <rect x="8" y="40" width="30" height="360" fill="url(#stripe)"/>
    </svg>
    <div class="front-brand">
      <div class="brand-name">HARGREAVE</div>
      <div class="brand-tagline">PROPERTY INVESTMENTS</div>
    </div>
  </section>

  <section class="card card-back" aria-label="Business card back">
    <div class="block back-band-top"></div>
    <div class="block back-band-bottom"></div>
    <div class="back-brand">
      <div class="brand-name">HARGREAVE</div>
      <div class="brand-tagline">PROPERTY INVESTMENTS</div>
    </div>
    <div class="contact">
      <div class="contact-name">Martin Hargreave</div>
      <div class="contact-role">MANAGER</div>
      <div>07700 900318</div>
      <div>www.hargreavehomes.example</div>
      <div>martin@hargreave.example</div>
    </div>
  </section>
</body>
</html>
```